Book Cover Design Project

I need a book cover for a book that we will be releasing in the next few months.

It is a business book aimed at small businesses and people who want to escape the 9 - 5 and start their own business.

We want it to look similar to: http://www.tolvanbrook.example/wp-content/uploads/2010/03/fold-up.jpg and also the book designs that I have uploaded images for.

I quite like the grey / charcoal background and the bright lime green colours from the Quiet Harbor logo that I have attached. However, anything bright would be good - I am prepared to be flexible with colours. The books I have attached are a high impact as well - being bright blue with white black font with a really cool font.

The book is titled:

The Lantern Shop Plan

By Dale Vortan

Still thinking of the tagline, for now just use "Start an Online Business in no time at all"

Room for a quote/testimonial on the front of the book at the bottom, and as well on the back.

For the back cover text just use dummy text and my photo that is attached for now as well.

Barcode ISBN on the back at the bottom - price will be $19.95

Needs to be in PSD so we can change the text from our end.

I really want to get a good template made that I can edit the text for as we are still developing the book, but I want to get the book cover done so I can start advertising that it will be arriving soon.

There will probably be alterations that I need help with later down the track so looking to work with someone closely on this, and I will pay you for any extra time down the track..

Sizes will probably be around: I think 20.5cm tall and 14cm wide would be good..

Not sure how thick for the spine, it will depend on how many words get cut off, but as an estimate probably 1.5CM..
Updates

Just added some more detail to the brief.. Please read it carefully.

Target Market(s)

small business owners, professionals who want to start their own business, soon to be entrepreneurs, entrepreneurs

Industry/Entity Type

Advertising

Requirements
Must have
• The Lantern Shop Plan

and Dale Vortan must be prominent.

Tag line should be look cool under the title.

Must be very modern and cool. Needs to catch people's eyes so needs to be really punchy.

Nice to have
• Maybe a clock or stopwatch icon would be cool to add in there so it isn't just plain.. Similar to like how the books have a cool icon with them that I have attached in the uploaded images.
Should not have
• I like simplicity, artistic and very high impact. It really needs to draw you in and catch your eye.

Don't use plain boring fonts. Although I like simplicity slick design is very important - I dont want it to be boring - it has to look high quality and expensive. Therefore do not use fonts like Arial, Times New Roman those really boring fonts that make it look cheap. If I was going to do something like that then I might as well do it myself.

If you want to see the quality of things that I am usually involved with look at the artwork for one of my events that I run called Daybreaker: http://www.daybreaker.example/daybreaker-festival-anthems-ft-loomsparrow-harvest-night-eve-metro-report/

That will give you an idea of what type of quality things that I am involved with, so you need to be up for the task..

```html
<!DOCTYPE html>
<html lang="en">
<head>
<meta charset="utf-8">
<title>The Lantern Shop Plan — Dale Vortan</title>
<link rel="stylesheet" href="https://fonts.googleapis.com/css2?family=Fira+Sans+Extra+Condensed:wght@700;800&family=Courgette&family=PT+Sans:ital@1&display=swap">
<style>
  :root {
    --lime: #16f20f;
    --charcoal-light: #6a6c68;
    --charcoal-mid: #4a4c4a;
    --charcoal-dark: #252827;
    --extrude: #b9b9b9;
    --extrude-dark: #8e8e8e;
    --paper: #f2f2f2;
  }
  * { margin: 0; padding: 0; box-sizing: border-box; }
  html, body { width: 820px; height: 1200px; overflow: hidden; background: var(--charcoal-dark); }
  .cover {
    position: relative;
    width: 820px;
    height: 1200px;
    overflow: hidden;
    background:
      radial-gradient(ellipse 70% 55% at 55% 40%, var(--charcoal-light) 0%, var(--charcoal-mid) 45%, var(--charcoal-dark) 100%);
    text-align: center;
  }
  .author {
    position: absolute;
    top: 22px; left: 0; right: 0;
    font-family: "Fira Sans Extra Condensed", sans-serif;
    font-weight: 800;
    font-size: 40px;
    letter-spacing: 0.9em;
    padding-left: 0.9em;
    color: var(--lime);
    font-variant: small-caps;
    line-height: 1.2;
  }
  .author .initial { font-size: 56px; }
  .title {
    font-family: "Fira Sans Extra Condensed", sans-serif;
    font-weight: 800;
    color: var(--lime);
    line-height: 1;
  }
  .title-the {
    position: absolute;
    top: 150px; left: 0; right: 0;
    font-size: 128px;
  }
  .title-main {
    position: absolute;
    top: 300px; left: 0; right: 0;
    font-size: 200px;
    letter-spacing: 2px;
    transform: scaleY(1.45);
    transform-origin: top center;
    text-shadow:
      -2px 1px 0 var(--extrude), -4px 2px 0 var(--extrude), -6px 3px 0 var(--extrude),
      -8px 4px 0 var(--extrude), -10px 5px 0 var(--extrude), -12px 6px 0 var(--extrude-dark),
      -14px 7px 0 var(--extrude-dark);
  }
  .title-sub {
    position: absolute;
    top: 636px; left: 0; right: 0;
    font-size: 46px;
    font-weight: 700;
    line-height: 1.02;
  }
  .tagline {
    position: absolute;
    top: 768px; left: 0; right: 0;
    font-family: "Courgette", cursive;
    font-size: 34px;
    line-height: 1.22;
    color: var(--paper);
  }
  .tagline .accent { color: var(--lime); }
  .testimonial {
    position: absolute;
    top: 952px; left: 70px; right: 70px;
    font-family: "PT Sans", sans-serif;
    font-style: italic;
    font-size: 26px;
    line-height: 1.3;
    color: var(--paper);
  }
</style>
</head>
<body>
  <main class="cover">
    <p class="author"><span class="initial">D</span>ale <span class="initial">V</span>ortan</p>

    <h1 class="title">
      <span class="title-the">THE</span>
      <span class="title-main">LANTERN</span>
      <span class="title-sub">SHOP<br>PLAN</span>
    </h1>

    <p class="tagline">Start an Online <span class="accent">Business</span><br>in no time at all</p>

    <p class="testimonial">place to add any quotes etc place to add any quotes etc place to add any quotes etc place to add any quotes etc place to add any quotes etc place to add any quotes etc</p>
  </main>
</body>
</html>
```